Independent Financial Advisor Billboard Campaign - Granite Bridge Financial

I am a local, independent financial advisor. My company is Granite Bridge Financial, located in Charleston, WV. My main source of revenue comes from those nearing or entering retirement that need assistance with financial planning and investment management. Many are looking to rollover their employer retirement plan into an IRA account. I would like a billboard design campaign that focuses on this type of client. Please see our website www.granitebridgefinancial-example.com for more information.

```html
<!DOCTYPE html>
<html lang="en">
<head>
<meta charset="utf-8">
<title>Granite Bridge Financial – Retirement Done Right Billboard</title>
<link rel="stylesheet" href="https://fonts.googleapis.com/css2?family=League+Spartan:wght@600;800&family=Montserrat:wght@500;600&display=swap">
<style>
  :root {
    --page-bg: #eceef2;
    --navy: #163d6b;
    --navy-deep: #0f2f57;
    --navy-light: #1f4c80;
    --tan: #c2936a;
    --white: #ffffff;
    --soft-white: #e9edf3;
    --brick: #9c5a3e;
    --brick-light: #b87552;
  }
  * { margin: 0; padding: 0; box-sizing: border-box; }
  html, body {
    width: 1050px;
    height: 1200px;
    overflow: hidden;
    background: var(--page-bg);
  }
  .canvas {
    position: relative;
    width: 1050px;
    height: 1200px;
  }
  .billboard {
    position: absolute;
    left: 35px;
    top: 457px;
    width: 980px;
    height: 286px;
    overflow: hidden;
    background: radial-gradient(ellipse at 35% 55%, var(--navy-light) 0%, var(--navy) 45%, var(--navy-deep) 100%);
  }
  .portrait {
    position: absolute;
    right: 0;
    top: 0;
    width: 215px;
    height: 286px;
    background: linear-gradient(160deg, var(--brick-light) 0%, var(--brick) 60%, #7e4631 100%);
  }
  .headline {
    position: absolute;
    left: 34px;
    top: 28px;
    font-family: "League Spartan", "Montserrat", sans-serif;
    font-weight: 800;
    font-size: 100px;
    line-height: 72px;
    letter-spacing: 0;
    text-transform: uppercase;
  }
  .headline-top { display: block; color: var(--white); }
  .headline-bottom { display: block; color: var(--tan); }
  .brand {
    position: absolute;
    left: 34px;
    top: 214px;
    display: flex;
    align-items: center;
    gap: 10px;
  }
  .brand-mark {
    width: 26px;
    height: 26px;
    background: var(--white);
  }
  .brand-name {
    font-family: "League Spartan", "Montserrat", sans-serif;
    font-weight: 600;
    font-size: 20px;
    color: var(--white);
    letter-spacing: 0.3px;
  }
  .contact {
    position: absolute;
    left: 358px;
    top: 192px;
  }
  .phone-row {
    display: flex;
    align-items: center;
    gap: 14px;
    margin-left: 5px;
  }
  .phone-icon { width: 34px; height: 34px; display: block; }
  .phone-number {
    font-family: "Montserrat", sans-serif;
    font-weight: 600;
    font-size: 41px;
    line-height: 40px;
    color: var(--white);
    letter-spacing: 0.5px;
  }
  .website {
    margin-top: 8px;
    font-family: "Montserrat", sans-serif;
    font-weight: 500;
    font-size: 14.5px;
    color: var(--soft-white);
    letter-spacing: 0.6px;
  }
</style>
</head>
<body>
<div class="canvas">
  <section class="billboard">
    <div class="portrait" role="img" aria-label="Portrait photo of the advisor in a white polo shirt in front of a brick wall"></div>

    <h1 class="headline">
      <span class="headline-top">Retirement</span>
      <span class="headline-bottom">Done Right!</span>
    </h1>

    <div class="brand">
      <span class="brand-mark"></span>
      <span class="brand-name">Granite Bridge Financial</span>
    </div>

    <div class="contact">
      <div class="phone-row">
        <svg class="phone-icon" viewBox="0 0 34 34" aria-hidden="true">
          <circle cx="17" cy="17" r="17" fill="var(--tan)"/>
          <path d="M11.5 9.5c.8-.6 1.8-.4 2.3.4l1.6 2.6c.4.7.3 1.6-.3 2.1l-1 .9c.8 1.8 2.3 3.4 4.1 4.3l.9-1c.5-.6 1.4-.7 2.1-.3l2.6 1.5c.8.5 1 1.5.4 2.3l-1 1.3c-.7.9-1.900 1.3-3 .9-4.6-1.6-8.2-5.2-9.8-9.8-.4-1.1 0-2.3.9-3z" fill="var(--navy)"/>
          <path d="M19 9.5a5.5 5.5 0 0 1 5.5 5.5M19 12.3a2.7 2.7 0 0 1 2.7 2.7" fill="none" stroke="var(--navy)" stroke-width="1.5" stroke-linecap="round"/>
        </svg>
        <span class="phone-number">304.555.0142</span>
      </div>
      <p class="website">www.granitebridgefinancial-example.com</p>
    </div>
  </section>
</div>
</body>
</html>
```